Business Card Design

I am a classical pilates instructor. I have a home studio, teach out a of a large studio downtown, and teach at on location corporate settings
I like my card to be very simple and clean.
I would like a silhouette of the picture I'm uploading on my design. In the upload section it looks like the picture is cut off and only showing a leg in the air...let me know if you can open up the entire picture.

Industry/Entity Type
Business
Contact Information for Business Card
Norah Fennick Pilates
Certified - The Pilates Hall of Marrow Creek
nf.fennick27@quillpost.example
555.314.7720

```html
<!DOCTYPE html>
<html lang="en">
<head>
<meta charset="utf-8">
<title>Norah Fennick Pilates – Business Card</title>
<link rel="stylesheet" href="https://fonts.googleapis.com/css2?family=Oswald:wght@400&family=Tinos&family=Roboto:wght@400&display=swap">
<style>
  :root {
    --page-bg: #ecebe8;
    --card-bg: #3e3e40;
    --band: #8b8b8d;
    --teal: #1db39f;
    --green: #7fb83f;
    --ink-light: #f2f2f2;
    --ink-soft: #d6d6d6;
    --photo-top: #ededed;
    --photo-mid: #bdbdbd;
    --photo-low: #9a9a9a;
  }
  html, body {
    margin: 0;
    width: 1200px;
    height: 929px;
    overflow: hidden;
    background: var(--page-bg);
  }
  .card {
    position: absolute;
    left: 100px;
    top: 179px;
    width: 1000px;
    height: 571px;
    border-radius: 28px;
    overflow: hidden;
    background: var(--card-bg);
    box-shadow: 0 6px 18px rgba(0,0,0,0.18);
  }
  .card__art {
    position: absolute;
    inset: 0;
  }
  .card__info {
    position: absolute;
    left: 84px;
    top: 150px;
  }
  .name {
    margin: 0;
    font-family: "Oswald", sans-serif;
    font-weight: 400;
    font-size: 54px;
    line-height: 1;
    color: var(--teal);
    text-transform: uppercase;
    letter-spacing: 1px;
  }
  .credential {
    margin: 10px 0 0 2px;
    font-family: "Tinos", serif;
    font-size: 24px;
    letter-spacing: 6px;
    color: var(--ink-light);
    text-transform: uppercase;
  }
  .studio {
    margin: 6px 0 0 2px;
    font-family: "Roboto", sans-serif;
    font-size: 18px;
    color: var(--green);
  }
  .contact {
    list-style: none;
    margin: 26px 0 0 2px;
    padding: 0;
    font-family: "Roboto", sans-serif;
    font-size: 18px;
    color: var(--ink-soft);
  }
  .contact__item {
    display: flex;
    align-items: center;
    gap: 16px;
    height: 32px;
  }
  .contact__icon {
    width: 22px;
    height: 22px;
    fill: var(--teal);
    flex: none;
  }
</style>
</head>
<body>
  <article class="card">
    <svg class="card__art" width="1000" height="571" viewBox="0 0 1000 571">
      <defs>
        <linearGradient id="beach-tones" x1="0" y1="0" x2="0" y2="1">
          <stop offset="0" stop-color="var(--photo-top)"/>
          <stop offset="0.62" stop-color="var(--photo-mid)"/>
          <stop offset="1" stop-color="var(--photo-low)"/>
        </linearGradient>
      </defs>
      <path class="photo-band" d="M 712 0 C 645 180, 598 380, 602 571 L 1000 571 L 1000 0 Z" fill="var(--band)"/>
      <path class="photo-frame" d="M 732 0 C 665 180, 618 380, 622 571 L 1000 571 L 1000 0 Z" fill="url(#beach-tones)" role="img" aria-label="Black and white photo of a pilates instructor in a shoulder-stand pose on a beach, legs raised toward the sky"/>
    </svg>

    <div class="card__info">
      <h1 class="name">Norah Fennick</h1>
      <p class="credential">Pilates Certified</p>
      <p class="studio">The Pilates Hall of Marrow Creek</p>
      <ul class="contact">
        <li class="contact__item">
          <svg class="contact__icon" viewBox="0 0 24 24" aria-hidden="true"><path d="M2 5h20v14H2z" fill="var(--teal)"/><path d="M3 6l9 7 9-7" fill="none" stroke="var(--card-bg)" stroke-width="1.6"/></svg>
          <span>nf.fennick27@quillpost.example</span>
        </li>
        <li class="contact__item">
          <svg class="contact__icon" viewBox="0 0 24 24" aria-hidden="true"><path d="M6.6 10.8c1.4 2.8 3.8 5.1 6.6 6.6l2.2-2.2c.3-.3.7-.4 1-.2 1.1.4 2.3.6 3.6.6.6 0 1 .4 1 1V20c0 .6-.4 1-1 1C10.6 21 3 13.4 3 4c0-.6.4-1 1-1h3.5c.6 0 1 .4 1 1 0 1.3.2 2.5.6 3.6.1.3 0 .7-.2 1z"/></svg>
          <span>555.314.7720</span>
        </li>
      </ul>
    </div>
  </article>
</body>
</html>
```